Flooring & Interior Design showroom

Just bought this business- Kestrel Lane Flooring & Interiors. Love our logo (we are on Kestrel Lane )and colors
Forest green, gold and black
Love that the back lists everything we do. We no longer have plenotilex but need to add in LVP/ SPC and need to take out vantor shadehub logo at the bottom and use the quib logo instead (maybe? open to suggestions)

Not in love with our cards- I want a higher end look
I hate the gradient poop color we have now.
Would love if they were all black - maybe or ??
or had a foil or embossing?

```html
<!DOCTYPE html>
<html lang="en">
<head>
<meta charset="utf-8">
<title>Kestrel Lane Flooring &amp; Interiors – Business Cards</title>
<link rel="stylesheet" href="https://fonts.googleapis.com/css2?family=Cormorant+Garamond:wght@600;700&family=Cinzel:wght@600;700&display=swap">
<style>
  :root {
    --backdrop: #3a3b3e;
    --card-black: #121212;
    --card-edge: #8a5a36;
    --forest: #0f4d2a;
    --forest-light: #1d6b3b;
    --gold: #e8cf5a;
    --ivory: #f4f1e8;
  }
  * { margin: 0; padding: 0; box-sizing: border-box; }
  html, body { width: 1200px; height: 801px; overflow: hidden; }
  body {
    background: var(--backdrop);
    font-family: "Cormorant Garamond", Georgia, serif;
    font-weight: 700;
    color: var(--ivory);
    position: relative;
  }
  .card {
    position: absolute;
    top: 50px;
    width: 400px;
    height: 700px;
    background: var(--card-black);
    border: 2px solid var(--card-edge);
    border-radius: 18px;
    overflow: hidden;
  }
  .card--front { left: 150px; }
  .card--back { left: 650px; }

  .sign-pole {
    position: absolute;
    top: 0; left: 26px;
    width: 16px; height: 100%;
    background: linear-gradient(90deg, #0a3a1f, var(--forest-light), #0a3a1f);
  }
  .brand {
    position: absolute;
    top: 40px; right: 30px;
    text-align: right;
  }
  .brand__name {
    display: flex; align-items: center; justify-content: flex-end; gap: 10px;
    font-size: 34px;
    letter-spacing: 1px;
    text-transform: uppercase;
    color: var(--gold);
  }
  .brand__mark {
    width: 14px; height: 14px;
    background: var(--forest-light);
  }
  .brand__trade {
    font-size: 17px;
    letter-spacing: 1.5px;
    text-transform: uppercase;
    margin-top: 4px;
  }
  .brand__tagline {
    font-size: 17px;
    color: var(--gold);
    margin-top: 2px;
  }

  .person { position: absolute; left: 70px; top: 230px; }
  .person__name {
    font-family: "Cinzel", Georgia, serif;
    font-size: 32px;
    color: var(--gold);
    letter-spacing: 1px;
  }
  .person__role { font-size: 20px; margin-top: 2px; }

  .contact { position: absolute; left: 70px; top: 340px; font-size: 21px; line-height: 1.35; }
  .contact__label { color: var(--gold); }
  .address { position: absolute; left: 70px; top: 470px; font-size: 20px; line-height: 1.35; }
  .license { position: absolute; left: 70px; bottom: 60px; font-size: 22px; color: var(--gold); }

  .main-phone {
    position: absolute; top: 180px; left: 0; width: 100%;
    text-align: center;
    font-size: 34px; letter-spacing: 6px;
  }
  .website {
    position: absolute; top: 228px; left: 0; width: 100%;
    text-align: center;
    font-size: 18px; color: var(--gold); letter-spacing: 0.5px;
  }
  .services {
    position: absolute; top: 285px; left: 30px; right: 20px;
    display: grid; grid-template-columns: 150px 1fr; column-gap: 12px;
  }
  .services ul { list-style: none; }
  .services li {
    font-size: 21px; line-height: 1.45;
    white-space: nowrap;
    display: flex; align-items: center; gap: 10px;
  }
  .services li::before {
    content: ""; width: 6px; height: 6px; border-radius: 50%;
    background: var(--gold); flex: none;
  }
  .partners {
    position: absolute; left: 40px; right: 40px; bottom: 40px;
    display: flex; justify-content: space-between; align-items: center;
  }
  .partner { font-size: 28px; color: var(--ivory); }
</style>
</head>
<body>

  <article class="card card--front">
    <div class="sign-pole" role="img" aria-label="Green street sign pole illustration"></div>
    <header class="brand">
      <div class="brand__name"><span class="brand__mark"></span>Kestrel Lane</div>
      <div class="brand__trade">Flooring &amp; Interiors</div>
      <div class="brand__tagline">Home Town Service Since 1979</div>
    </header>
    <div class="person">
      <div class="person__name">MILES HARLAN</div>
      <div class="person__role">Salesperson</div>
    </div>
    <div class="contact">
      <div><span class="contact__label">Store:</span> 555.214.0380</div>
      <div><span class="contact__label">Cell:</span> 555.617.2294</div>
      <div><span class="contact__label">Fax:</span> 555.214.0391</div>
    </div>
    <div class="address">
      <div>214 Kestrel Ln, Harbor Cove,</div>
      <div>CA 90210</div>
      <div>miles@kestrellaneflooring.com</div>
    </div>
    <div class="license">CA Lic # 412087</div>
  </article>

  <article class="card card--back">
    <header class="brand">
      <div class="brand__name"><span class="brand__mark"></span>Kestrel Lane</div>
      <div class="brand__trade">Flooring &amp; Interiors</div>
      <div class="brand__tagline">Home Town Service Since 1979</div>
    </header>
    <div class="main-phone">555.214.0380</div>
    <div class="website">www.kestrellaneflooring.com</div>
    <section class="services">
      <ul>
        <li>Carpet</li><li>Hardwood</li><li>Fabric</li><li>Vinyl</li>
        <li>Verticals</li><li>Shutters</li><li>Upholstery</li>
        <li>Bed Spreads</li><li>Pillows</li>
      </ul>
      <ul>
        <li>Area rugs</li><li>Cork</li><li>Laminate</li><li>Blinds</li>
        <li>Sheers</li><li>Draperies</li><li>Valances</li>
        <li>LVP/ SPC</li><li>Motorized Shades</li>
      </ul>
    </section>
    <footer class="partners">
      <div class="partner">Lumenford</div>
      <div class="partner">Quib</div>
    </footer>
  </article>

</body>
</html>
```